Securities Exam Training Banner Add for Promoline campaign

We need a banner ad design to use for a remarketing campaign in Fennic Promoline. We are a securities exam training provider that provides online training across the U.S. and Canada. Banner ad designs should be consistent in color and concept with our website: www.brevanlearnhub.example.

Approved ad copy:

"Pass on your first attempt. Experience what you are missing with your current training provider."

"Pass the Tier 4 on your first attempt with our industry-leading training program. "

-High quality audio lecture.
-Interactive visual presentations.
-Comprehensive course textbook.

"We give you everything you need to pass on your first attempt."

Deliverables:

-Ad Sizes (250x250; 200x200; 468x60; 728x90; 300x250; 336x280; 120x600; 160x600)
-.gif, .jpg, .png, or .swf
-50kb or smaller

Theme:

-Design should reflect financial security, confidence in the product, and differentiation from the "rest of the industry."

Target Market(s)

People who are training for securities exams in the financial industry. e.g. people who work for Dorrance Pell, Hadley Fenwick, Corvin Tate, etc..

Industry/Entity Type

Financial

Requirements
Must have
• Company Logo and phrase "The leader in securities exam prep"
Strong call to action on final screen (Buy Now).

```html
<!DOCTYPE html>
<html lang="en">
<head>
<meta charset="utf-8">
<title>Brevan Learnhub – Promoline Banner Set 250x250</title>
<link rel="stylesheet" href="https://fonts.googleapis.com/css2?family=Libre+Baskerville:wght@400;700&family=Open+Sans:wght@300&display=swap">
<style>
  :root {
    --canvas: #ffffff;
    --ink-blue: #1d4f9c;
    --ink-gray: #4a4a4a;
    --brand-gray: #3a3a3a;
    --brand-square: #2d63ad;
    --ridge-dark: #8d8f93;
    --ridge-light: #d3d5d8;
    --cta-top: #5a8fcf;
    --cta-bottom: #1f4f92;
    --label-gray: #c3c3c3;
  }
  * { margin: 0; padding: 0; box-sizing: border-box; }
  html, body {
    width: 1200px; height: 337px; overflow: hidden;
    background: var(--canvas);
  }
  .board { position: relative; width: 1200px; height: 337px; }

  .banner {
    position: absolute; top: 5px; width: 284px; height: 284px;
    background: #fff; overflow: hidden;
    font-family: "Libre Baskerville", "Times New Roman", serif;
  }
  .banner--one   { left: 4px; }
  .banner--two   { left: 307px; }
  .banner--three { left: 611px; }
  .banner--four  { left: 914px; }

  .banner__photo { position: absolute; left: 0; top: 0; width: 284px; height: 160px; }
  .photo--ticker {
    background:
      radial-gradient(ellipse 60% 45% at 30% 45%, rgba(120,200,255,0.55), transparent 70%),
      radial-gradient(ellipse 40% 35% at 80% 35%, rgba(90,170,255,0.45), transparent 70%),
      linear-gradient(160deg, #061c4e 0%, #1456b8 50%, #0a2a66 100%);
  }
  .photo--traders {
    background:
      radial-gradient(ellipse 35% 50% at 35% 55%, rgba(60,60,70,0.55), transparent 75%),
      radial-gradient(ellipse 30% 45% at 65% 50%, rgba(80,80,90,0.45), transparent 75%),
      linear-gradient(180deg, #6f7782 0%, #b7bec7 55%, #eef0f2 100%);
  }
  .photo--chart {
    background:
      radial-gradient(ellipse 45% 40% at 65% 45%, rgba(255,255,255,0.95), transparent 75%),
      radial-gradient(ellipse 35% 35% at 15% 90%, rgba(70,110,180,0.8), transparent 75%),
      linear-gradient(150deg, #f3f4f6 0%, #d4d9e0 60%, #a9b8cf 100%);
  }
  .photo--success {
    background:
      radial-gradient(ellipse 30% 45% at 78% 40%, rgba(180,185,195,0.6), transparent 75%),
      radial-gradient(ellipse 45% 25% at 45% 70%, rgba(230,90,80,0.25), transparent 75%),
      linear-gradient(150deg, #ffffff 0%, #eceef0 55%, #dcdfe3 100%);
  }

  .banner__ridge { position: absolute; left: 0; top: 100px; width: 284px; height: 70px; }

  .banner__copy {
    position: absolute; left: 0; top: 162px; width: 284px;
    text-align: center; font-size: 12px; line-height: 14px; color: var(--ink-gray);
  }
  .banner__copy .lead { color: var(--ink-blue); font-size: 13.5px; }
  .banner__copy--list { top: 160px; line-height: 16px; }
  .banner__copy--two { top: 166px; }

  .brand {
    position: absolute; left: 42px; top: 214px; height: 44px;
    display: flex; align-items: center; gap: 10px;
  }
  .brand__square { width: 42px; height: 42px; background: var(--brand-square); }
  .brand__name {
    color: var(--brand-gray); font-size: 19.5px; line-height: 20px;
    letter-spacing: 0.2px; font-weight: 400;
  }

  .cta {
    position: absolute; left: 0; top: 266px; width: 284px; height: 18px;
    background: linear-gradient(var(--cta-top), var(--cta-bottom));
    color: #fff; font-size: 8px; letter-spacing: 1.2px;
    text-align: center; line-height: 18px; text-transform: uppercase;
  }

  .size-label {
    position: absolute; left: 8px; top: 296px;
    font-family: "Open Sans", Arial, sans-serif; font-weight: 300;
    font-size: 26px; color: var(--label-gray);
  }
</style>
</head>
<body>
<div class="board">

  <section class="banner banner--one">
    <div class="banner__photo photo--ticker" role="img" aria-label="Close-up of a stock market ticker board with glowing price figures"></div>
    <svg class="banner__ridge" viewBox="0 0 284 70" aria-hidden="true">
      <polygon points="0,46 68,22 108,40 166,8 232,30 284,14 284,70 0,70" fill="var(--ridge-dark)"/>
      <polygon points="0,54 68,30 108,48 166,16 232,38 284,22 284,70 0,70" fill="var(--ridge-light)"/>
      <polygon points="0,62 68,40 108,58 166,28 232,48 284,34 284,70 0,70" fill="#fff"/>
    </svg>
    <p class="banner__copy">
      <span class="lead">Pass on your first attempt.</span><br>
      Experience what you are missing<br>
      with your current training provider.
    </p>
    <div class="brand"><span class="brand__square"></span><span class="brand__name">BREVAN<br>LEARNHUB</span></div>
    <div class="cta">Click here to learn more</div>
  </section>

  <section class="banner banner--two">
    <div class="banner__photo photo--traders" role="img" aria-label="Two traders studying a screen together in an office"></div>
    <svg class="banner__ridge" viewBox="0 0 284 70" aria-hidden="true">
      <polygon points="0,46 68,22 108,40 166,8 232,30 284,14 284,70 0,70" fill="var(--ridge-dark)"/>
      <polygon points="0,54 68,30 108,48 166,16 232,38 284,22 284,70 0,70" fill="var(--ridge-light)"/>
      <polygon points="0,62 68,40 108,58 166,28 232,48 284,34 284,70 0,70" fill="#fff"/>
    </svg>
    <p class="banner__copy banner__copy--two">
      Pass the Tier 4 on <span class="lead">your first attempt</span><br>
      with our industry-leading<br>
      training program.
    </p>
    <div class="brand"><span class="brand__square"></span><span class="brand__name">BREVAN<br>LEARNHUB</span></div>
    <div class="cta">Click here to learn more</div>
  </section>

  <section class="banner banner--three">
    <div class="banner__photo photo--chart" role="img" aria-label="Hand with a pen pointing at a financial chart on a screen"></div>
    <svg class="banner__ridge" viewBox="0 0 284 70" aria-hidden="true">
      <polygon points="0,46 68,22 108,40 166,8 232,30 284,14 284,70 0,70" fill="var(--ridge-dark)"/>
      <polygon points="0,54 68,30 108,48 166,16 232,38 284,22 284,70 0,70" fill="var(--ridge-light)"/>
      <polygon points="0,62 68,40 108,58 166,28 232,48 284,34 284,70 0,70" fill="#fff"/>
    </svg>
    <p class="banner__copy banner__copy--list">
      -High quality <span class="lead">audio lecture.</span><br>
      -<span class="lead">Interactive</span> visual presentations.<br>
      -Comprehensive <span class="lead">course textbook.</span>
    </p>
    <div class="brand"><span class="brand__square"></span><span class="brand__name">BREVAN<br>LEARNHUB</span></div>
    <div class="cta">Click here to learn more</div>
  </section>

  <section class="banner banner--four">
    <div class="banner__photo photo--success" role="img" aria-label="Cheering businessman beside a laptop and a rising red chart line"></div>
    <svg class="banner__ridge" viewBox="0 0 284 70" aria-hidden="true">
      <polygon points="0,46 68,22 108,40 166,8 232,30 284,14 284,70 0,70" fill="var(--ridge-dark)"/>
      <polygon points="0,54 68,30 108,48 166,16 232,38 284,22 284,70 0,70" fill="var(--ridge-light)"/>
      <polygon points="0,62 68,40 108,58 166,28 232,48 284,34 284,70 0,70" fill="#fff"/>
    </svg>
    <p class="banner__copy banner__copy--two">
      <span class="lead">We give you everything</span><br>
      you need to pass on your first attempt.
    </p>
    <div class="brand"><span class="brand__square"></span><span class="brand__name">BREVAN<br>LEARNHUB</span></div>
    <div class="cta">Click here to learn more</div>
  </section>

  <p class="size-label">250x250</p>
</div>
</body>
</html>
```